Organic Food Packaging for Bulk Nuts, Seeds, Dried fruit

We need a simple yet creative packaging design for our vitanest brand. The packaging will be for stand up bags. We would like a very simply design that we can use for all of our packaging needs. The size of the pouch is 6" wide by 12" tall. You can visit our site. www.vitanest.example to get some ideas. Here are some packaging ideas we do like. https://wrappers.sampleboard.example/contest/4720948https://designmart.example/item/dry-fuits-bag-packaging/27939773

Target Market(s)

organic foods, health food, green, speciality and gourmet shops

Industry/Entity Type

Food Production

Font styles to use
Sans Serif

Requirements
Must have
• We need space in the middle of the pouch to be white so we can apply labels on it.
Nice to have
• Simple vines, leaves, gray patterns, 2-3 color design will be best. We would like a see through window. I have attached our logo.
Should not have
• many colors or lots of background colors.

```html
<!DOCTYPE html>
<html lang="en">
<head>
<meta charset="utf-8">
<title>Vitanest stand-up pouch</title>
<link rel="stylesheet" href="https://fonts.googleapis.com/css2?family=Josefin+Sans:wght@300;400;600&display=swap">
<style>
  :root {
    --stage: #4a4a4a;
    --pouch-grey: #8c8c8e;
    --pouch-grey-light: #9a9a9c;
    --pouch-grey-edge: #7e7e80;
    --band-dark: #5e5e60;
    --pouch-red: #9b1422;
    --pouch-red-deep: #7e0f1b;
    --accent-yellow: #f5c400;
    --label-white: #ffffff;
    --ink-light: #ffffff;
    --ink-dark: #3a3a3a;
    --ribbon-ink: #6b0c15;
  }
  html, body {
    margin: 0;
    padding: 0;
    width: 1200px;
    height: 1200px;
    overflow: hidden;
    background: var(--stage);
  }
  .canvas {
    position: relative;
    width: 1200px;
    height: 1200px;
  }
  .pouch {
    position: absolute;
    left: 374px;
    top: 146px;
    width: 452px;
    height: 908px;
  }
  .brand-name {
    font-family: "Josefin Sans", sans-serif;
    font-weight: 400;
    font-size: 54px;
    letter-spacing: 1px;
    fill: var(--ink-light);
  }
  .brand-tagline {
    font-family: "Josefin Sans", sans-serif;
    font-weight: 400;
    font-size: 14px;
    letter-spacing: 6px;
    fill: var(--ink-dark);
  }
  .net-label {
    font-family: "Josefin Sans", sans-serif;
    font-weight: 300;
    font-size: 10px;
    fill: var(--ink-light);
  }
  .net-value {
    font-family: "Josefin Sans", sans-serif;
    font-weight: 300;
    font-size: 22px;
    fill: var(--ink-light);
  }
  .ribbon-text {
    font-family: "Josefin Sans", sans-serif;
    font-weight: 400;
    font-size: 20px;
    fill: var(--ribbon-ink);
  }
</style>
</head>
<body>
<main class="canvas">
  <svg class="pouch" viewBox="0 0 565 1135" xmlns="http://www.w3.org/2000/svg">
    <defs>
      <clipPath id="pouch-shape">
        <rect x="0" y="0" width="565" height="1135" rx="6"/>
      </clipPath>
      <linearGradient id="grey-sheen" x1="0" y1="0" x2="1" y2="0">
        <stop offset="0" stop-color="var(--pouch-grey-edge)"/>
        <stop offset="0.5" stop-color="var(--pouch-grey-light)"/>
        <stop offset="1" stop-color="var(--pouch-grey-edge)"/>
      </linearGradient>
      <linearGradient id="red-sheen" x1="0" y1="0" x2="1" y2="0">
        <stop offset="0" stop-color="var(--pouch-red-deep)"/>
        <stop offset="0.45" stop-color="var(--pouch-red)"/>
        <stop offset="1" stop-color="var(--pouch-red-deep)"/>
      </linearGradient>
    </defs>

    <g clip-path="url(#pouch-shape)">
      <rect class="panel-grey" x="0" y="0" width="565" height="1135" fill="url(#grey-sheen)"/>

      <g class="seal-lines" stroke="#6e6e70" stroke-width="1.5">
        <line x1="15" y1="30" x2="555" y2="30"/>
        <line x1="15" y1="36" x2="555" y2="36"/>
        <line x1="15" y1="42" x2="555" y2="42"/>
        <line x1="15" y1="48" x2="555" y2="48"/>
      </g>

      <path class="band-dark" d="M0 270 C 170 300, 330 430, 420 600 C 460 640, 520 620, 565 612 L565 1135 L0 1135 Z" fill="var(--band-dark)"/>
      <path class="panel-red" d="M0 325 C 150 390, 240 520, 330 640 C 400 700, 480 690, 565 678 L565 1135 L0 1135 Z" fill="url(#red-sheen)"/>

      <!-- decorative dots in the three-colour palette -->
      <circle class="dot-large" cx="410" cy="458" r="125" fill="var(--accent-yellow)" opacity="0.5"/>
      <circle class="dot-edge" cx="552" cy="648" r="21" fill="var(--accent-yellow)"/>
      <circle class="dot-small-left" cx="58" cy="682" r="22" fill="var(--label-white)" opacity="0.55"/>
      <circle class="dot-deep" cx="105" cy="800" r="68" fill="var(--pouch-red-deep)" stroke="var(--accent-yellow)" stroke-width="3"/>
      <circle class="dot-right" cx="460" cy="770" r="48" fill="var(--accent-yellow)"/>
      <circle class="dot-low" cx="378" cy="872" r="22" fill="var(--accent-yellow)"/>

      <!-- white label area -->
      <g class="label-area">
        <circle cx="287" cy="657" r="192" fill="var(--label-white)" role="img" aria-label="White label area for product sticker"/>
        <circle cx="287" cy="657" r="192" fill="none" stroke="var(--accent-yellow)" stroke-width="7"/>
      </g>

      <g class="brand">
        <circle cx="112" cy="234" r="8" fill="var(--ink-light)"/>
        <text class="brand-name" x="296" y="256" text-anchor="middle">VITANEST</text>
        <text class="brand-tagline" x="284" y="297" text-anchor="middle">ABOUT YOUR PRODUCT</text>
      </g>

      <g class="net-content">
        <text class="net-label" x="533" y="962" text-anchor="end">net content</text>
        <text class="net-value" x="533" y="984" text-anchor="end">00.kg</text>
      </g>

      <path class="ribbon" d="M0 997 C 190 1005, 380 1002, 565 994 L565 1032 C 380 1040, 190 1043, 0 1035 Z" fill="var(--accent-yellow)"/>
      <text class="ribbon-text" x="288" y="1035" text-anchor="middle">LOREM IPSUM TEXT HERE</text>

      <g class="seal-lines" stroke="#6d0c17" stroke-width="1.5" fill="none">
        <path d="M0 1080 C 190 1088, 380 1086, 565 1078"/>
        <path d="M0 1087 C 190 1095, 380 1093, 565 1085"/>
        <path d="M0 1094 C 190 1102, 380 1100, 565 1092"/>
      </g>
    </g>
  </svg>
</main>
</body>
</html>
```